Business Card for Bright Meadow Lawn & Landscape

Double Sided Card Design - I think one side of the card should be cleaner, with logo, contact info, and "Complete Residential & Commercial Landscape Services", and on the other side it should list the services we offer:

- Lawn Care & Mowing
- Hedge & Shrub Trimming
- Leaf Removal & Clean Up
- Aeration & Sod
- Mulch & Rock Installations
- Landscape Installations & Renovations
- Commercial Snow Removal

Please make it clean and very professional... don't want it too be too busy, but want to tell them what we do.

Target Market(s)

Residential and Commercial

Industry/Entity Type

Landscape

Contact Information for Business Card

Fully Insured
Tom Berrigan
410-555-0198
Tberrigan07@mailbox-example.com

Requirements
Must have
• Double Sided, Cleaner on one side, more information and text on the other side.

```html
<!DOCTYPE html>
<html lang="en">
<head>
<meta charset="utf-8">
<title>Bright Meadow Lawn &amp; Landscape — Business Card</title>
<link href="https://fonts.googleapis.com/css2?family=Cinzel:wght@400;700&family=Crimson+Text:ital,wght@0,400;0,700;1,400&display=swap" rel="stylesheet">
<style>
  :root{
    --backdrop:#8a7658;
    --card:#0b0b0b;
    --green:#7cb83a;
    --green-deep:#5f9a26;
    --white:#ffffff;
    --grey:#c9c9c9;
    --ink:#111111;
  }
  *{box-sizing:border-box;margin:0;padding:0}
  html,body{width:900px;height:1200px;overflow:hidden}
  body{background:var(--backdrop);position:relative;font-family:"Crimson Text",serif}
  .card{position:absolute;left:60px;width:780px;height:445px;background:var(--card);overflow:hidden;box-shadow:0 10px 30px rgba(0,0,0,.35)}
  .card--front{top:125px}
  .card--back{top:630px}

  /* front */
  .brand{position:absolute;top:28px;left:0;width:100%;text-align:center}
  .brand__mark{width:104px;height:104px;margin:0 auto 14px;display:block}
  .brand__name{font-family:"Cinzel",serif;font-weight:400;font-size:42px;color:var(--white);letter-spacing:1px;line-height:1}
  .brand__sub{font-family:"Cinzel",serif;font-size:24px;color:var(--grey);letter-spacing:3px;margin-top:8px}
  .brand__note{font-style:italic;color:var(--green);font-size:18px;margin-top:4px}
  .contact{position:absolute;top:292px;left:0;width:100%;display:flex;justify-content:center;align-items:center;gap:22px}
  .contact__name{font-family:"Cinzel",serif;font-size:24px;color:var(--green);letter-spacing:1px}
  .contact__divider{width:2px;height:54px;background:var(--grey)}
  .contact__lines{font-size:16px;color:var(--white);line-height:1.55}
  .contact__line{display:flex;align-items:center;gap:8px}
  .contact__line svg{width:14px;height:14px;fill:var(--green)}
  .tagline{position:absolute;top:372px;left:0;width:100%;height:38px;background:var(--green);border-top:4px solid var(--white);display:flex;align-items:center;justify-content:center}
  .tagline__text{font-family:"Crimson Text",serif;font-weight:700;font-size:21px;color:var(--ink);letter-spacing:1.5px;text-transform:uppercase}

  /* back */
  .back-mark{position:absolute;left:58px;top:92px;width:240px;text-align:center}
  .back-mark svg{width:200px;height:200px;display:block;margin:0 auto}
  .back-mark__name{font-family:"Cinzel",serif;font-size:22px;color:var(--white);margin-top:14px;letter-spacing:1px}
  .services{position:absolute;left:380px;top:78px;list-style:none;border-left:3px solid var(--green);padding-left:26px}
  .services__item{font-size:22px;color:var(--white);line-height:1.6}
</style>
</head>
<body>
  <section class="card card--front" aria-label="Card front">
    <div class="brand">
      <svg class="brand__mark" viewBox="0 0 104 104" aria-hidden="true">
        <circle cx="52" cy="52" r="46" fill="none" stroke="var(--green)" stroke-width="10"/>
      </svg>
      <div class="brand__name">Bright Meadow</div>
      <div class="brand__sub">Lawn &amp; Landscape</div>
      <div class="brand__note">Fully Insured</div>
    </div>
    <div class="contact">
      <div class="contact__name">Tom Berrigan</div>
      <div class="contact__divider"></div>
      <div class="contact__lines">
        <div class="contact__line">
          <svg viewBox="0 0 24 24" aria-hidden="true"><path d="M6.6 10.8a15 15 0 0 0 6.6 6.6l2.2-2.2a1 1 0 0 1 1-.25 11.4 11.4 0 0 0 3.6.57 1 1 0 0 1 1 1V20a1 1 0 0 1-1 1A17 17 0 0 1 3 4a1 1 0 0 1 1-1h3.5a1 1 0 0 1 1 1c0 1.25.2 2.45.57 3.6a1 1 0 0 1-.25 1z"/></svg>
          <span>410-555-0198</span>
        </div>
        <div class="contact__line">
          <svg viewBox="0 0 24 24" aria-hidden="true"><path d="M2 5h20v14H2z M2 5l10 8 10-8" fill="var(--green)"/><path d="M3 6l9 7 9-7" fill="none" stroke="var(--card)" stroke-width="1.6"/></svg>
          <span>Tberrigan07@mailbox-example.com</span>
        </div>
      </div>
    </div>
    <div class="tagline"><span class="tagline__text">Complete Residential &amp; Commercial Landscape Services</span></div>
  </section>

  <section class="card card--back" aria-label="Card back">
    <div class="back-mark">
      <svg viewBox="0 0 200 200" aria-hidden="true">
        <circle cx="100" cy="100" r="88" fill="none" stroke="var(--green)" stroke-width="18"/>
      </svg>
      <div class="back-mark__name">Bright Meadow</div>
    </div>
    <ul class="services">
      <li class="services__item">Lawn Care &amp; Mowing</li>
      <li class="services__item">Hedge &amp; Shrub Trimming</li>
      <li class="services__item">Leaf Removal &amp; Clean Up</li>
      <li class="services__item">Aeration &amp; Sod</li>
      <li class="services__item">Mulch &amp; Rock Installations</li>
      <li class="services__item">Landscape Installations &amp; Renovations</li>
      <li class="services__item">Commercial Snow Removal</li>
    </ul>
  </section>
</body>
</html>
```